A Maple Syrup Label for a Local Buniness

We are looking for a label for our maple syrup business. Our business currently sells honey, and we are expanding into maple syrup. Our Business name is "Brackley Honey" and we currently have a logo attached below. We would like to incorporate the bee and BH part, but the label could also read "Brackley Farms" with the words maple syrup. We do not want consumers to confuse the maple syrup jars with the honey jars. It should be clear that the jars contain maple syrup. We are open to new designs as well.

```html
<!DOCTYPE html>
<html lang="en">
<head>
<meta charset="utf-8">
<title>Brackley Honey – Maple Syrup Label</title>
<link rel="stylesheet" href="https://fonts.googleapis.com/css2?family=Libre+Baskerville:wght@400;700&family=Sacramento&display=swap">
<style>
  :root {
    --backdrop: #e4e4e4;
    --label-black: #1d1d1b;
    --label-gold: #f2c12e;
    --label-white: #ffffff;
    --ink: #1d1d1b;
  }
  * { margin: 0; padding: 0; box-sizing: border-box; }
  html, body {
    width: 1200px;
    height: 848px;
    overflow: hidden;
    background: var(--backdrop);
  }
  .canvas {
    position: relative;
    width: 1200px;
    height: 848px;
    background: var(--backdrop);
  }
  .label {
    position: absolute;
    left: 297px;
    top: 44px;
    width: 605px;
    height: 760px;
  }
  .label-frame {
    position: absolute;
    inset: 0;
    width: 100%;
    height: 100%;
  }
  .brand-emblem {
    position: absolute;
    left: 50%;
    top: 150px;
    width: 120px;
    height: 120px;
    margin-left: -60px;
    border-radius: 50%;
    background: var(--label-gold);
  }
  .brand-name {
    position: absolute;
    left: 0;
    right: 0;
    top: 300px;
    text-align: center;
    font-family: "Libre Baskerville", Georgia, serif;
    font-weight: 400;
    font-size: 54px;
    line-height: 68px;
    letter-spacing: 1px;
    color: var(--ink);
    text-transform: uppercase;
  }
  .product-name {
    position: absolute;
    left: 0;
    right: 0;
    top: 468px;
    text-align: center;
    font-family: "Sacramento", cursive;
    font-size: 76px;
    line-height: 90px;
    color: var(--ink);
  }
  .maple-leaf {
    position: absolute;
    left: 50%;
    top: 580px;
    width: 100px;
    height: 105px;
    margin-left: -50px;
    background: var(--label-black);
  }
</style>
</head>
<body>
<main class="canvas">
  <section class="label">
    <svg class="label-frame" viewBox="0 0 430 540" aria-hidden="true">
      <polygon points="0,120 120,0 310,0 430,120 430,420 310,540 120,540 0,420" fill="var(--label-black)"/>
      <polygon points="6,122 122,6 308,6 424,122 424,418 308,534 122,534 6,418" fill="none" stroke="var(--label-gold)" stroke-width="2.5"/>
      <polygon points="26,131 131,26 299,26 404,131 404,409 299,514 131,514 26,409" fill="var(--label-white)" stroke="var(--label-gold)" stroke-width="3"/>
    </svg>
    <div class="brand-emblem" aria-hidden="true"></div>
    <h1 class="brand-name">Brackley<br>Honey</h1>
    <p class="product-name">Maple Syrup</p>
    <div class="maple-leaf" role="img" aria-label="Black maple leaf symbol"></div>
  </section>
</main>
</body>
</html>
```